Business Card Design for BT Wine:

I'm looking for a card that has the following.
Front:
- Merlot Colored
- stripe down the middle in silver or gold flake
- BT in block like thick letters with gold or silver flake above stripe
-Wine: below stripe
- a grape bunch that is at the end of the stripe that is made so it can be printed as embossed
Back:
- line down the middle of card in Merlot, card is white background
- to the left Marla Boyce, (next line) Owner, (next line) Certified Sommelier, GRV
- to the right (listed) restaurant consulting, wine tours, personal tastings, event planning, personal wine buying
- add embossed grape bunch
Also, looking for a piece that slides over like a envelope for a room key for a hotel that says "We met @ DUNVAL" and possibly a file for that, that I can edit.
Would like card to be printed on a thicker cardstock

```html
<!DOCTYPE html>
<html lang="en">
<head>
<meta charset="utf-8">
<title>BT Wine — Business Card</title>
<link href="https://fonts.googleapis.com/css2?family=PT+Serif:wght@400;700&display=swap" rel="stylesheet">
<style>
  :root {
    --backdrop: #2b2b2b;
    --merlot: #4b1831;
    --merlot-mid: #6e3553;
    --merlot-soft: #8c5a75;
    --silver: #b9b9bd;
    --silver-dark: #8e8e93;
    --paper: #f4f3f3;
    --ink: #1f1f1f;
    --ink-soft: #555;
  }
  * { box-sizing: border-box; margin: 0; padding: 0; }
  html, body {
    width: 1200px; height: 814px; overflow: hidden;
    background: var(--backdrop);
    font-family: "PT Serif", Georgia, serif;
  }
  .sheet {
    width: 1200px; height: 814px;
    display: flex; align-items: center; justify-content: center; gap: 56px;
  }
  .card {
    position: relative;
    width: 520px; height: 297px;
    border-radius: 3px;
    overflow: hidden;
    box-shadow: 0 18px 40px rgba(0,0,0,.45);
  }

  /* Front */
  .card--front { background: var(--merlot); }
  .front__stripe {
    position: absolute; left: 0; top: 148px;
    width: 398px; height: 3px;
    background: linear-gradient(90deg, var(--silver-dark), var(--silver));
  }
  .front__name {
    position: absolute; left: 0; width: 400px; top: 76px;
    text-align: center;
    font-size: 52px; font-weight: 400; letter-spacing: 3px;
    color: var(--silver);
  }
  .front__grapes {
    position: absolute; left: 396px; top: 112px;
    width: 80px; height: 110px;
    border-radius: 40% 40% 50% 50%;
    background: radial-gradient(circle at 45% 40%, #2a0f1c, #14060d);
  }

  /* Back */
  .card--back { background: var(--paper); }
  .back__person {
    position: absolute; left: 38px; top: 62px;
    color: var(--ink);
  }
  .back__name { font-size: 20px; font-weight: 400; }
  .back__name strong { font-weight: 700; }
  .back__role { font-size: 11px; color: var(--ink-soft); line-height: 1.3; }
  .back__vine {
    position: absolute; left: 292px; top: 44px;
    width: 2px; height: 210px;
    background: var(--merlot-mid);
  }
  .back__grapes {
    position: absolute; width: 54px; height: 56px;
    border-radius: 45%;
    background: radial-gradient(circle at 45% 40%, var(--merlot-soft), var(--merlot-mid));
  }
  .back__grapes--top { left: 290px; top: 20px; }
  .back__grapes--bottom { left: 244px; top: 222px; }
  .back__services {
    position: absolute; left: 318px; top: 92px;
    list-style: none;
    font-size: 13px; line-height: 1.45; color: var(--ink);
  }
</style>
</head>
<body>
  <main class="sheet">
    <section class="card card--front" aria-label="Card front">
      <p class="front__name">BT Wine</p>
      <div class="front__stripe"></div>
      <div class="front__grapes" role="img" aria-label="Embossed grape bunch with vine leaf"></div>
    </section>

    <section class="card card--back" aria-label="Card back">
      <div class="back__person">
        <h1 class="back__name">Marla <strong>Boyce</strong></h1>
        <p class="back__role">Owner<br>Certified Sommelier, GRV</p>
      </div>
      <div class="back__vine"></div>
      <div class="back__grapes back__grapes--top" role="img" aria-label="Grape bunch with leaf"></div>
      <div class="back__grapes back__grapes--bottom" role="img" aria-label="Grape bunch with leaf"></div>
      <ul class="back__services">
        <li>Restaurant consulting</li>
        <li>Wine tours</li>
        <li>Personal tastings</li>
        <li>Event planning</li>
        <li>Personal wine buying</li>
      </ul>
    </section>
  </main>
</body>
</html>
```